High profile consulting company needs a Business Card Design

I need a business card design for a coaching /consulting company. We specialize in changing behaviors. Our services include therapy, workshops, life coaching, etc.

Check out our website to get a feel for our personality. www.tidewaterguidance.com

The new logo will be attached to the website soon, I have attached the new logo for your use on the business card.
Updates

I forgot to provide you with the company email under the "must have" section for the business card.  The website is:

 www.tidewaterguidance.com

I understand there's some trouble with the logo I uploaded.  I will try that again.  Thank you for your efforts.

Lauren

Thank you for some of your questions.  I prefer a one sided business card, and tend to like the white backgrounds.

I also made 2 small changes to the content.  

add MFT after the name:  Lauren Pettigrew, MFT

and the tag line needed more clarity once I saw it.  Please change it to:  Improving performance by strengthening relationships and changing behaviors.

Thank you,
Lauren

Industry/Entity Type

Business

Requirements
Must have
• logo
Phone number: 321-555-0164
email: Lauren@tidewaterguidance.com
Lauren Pettigrew, MFT
President
Nice to have
• Improving performance by strengthening relationships and changing behaviors.

```html
<!DOCTYPE html>
<html lang="en">
<head>
<meta charset="utf-8">
<title>Tidewater Guidance – Business Card</title>
<link rel="stylesheet" href="https://fonts.googleapis.com/css2?family=Jost:wght@400;500&display=swap">
<style>
  :root {
    --page: #e9e7e3;
    --card-grey: #6a6a6c;
    --card-white: #fbfbfb;
    --panel: #f3f3f3;
    --ink-dark: #3a3a3c;
    --ink-mid: #5c5c5e;
    --band-grey: #6a6a6c;
    --accent-green: #1d7a5b;
    --on-grey: #f4f4f4;
  }
  * { box-sizing: border-box; margin: 0; padding: 0; }
  html, body { width: 1200px; height: 900px; overflow: hidden; }
  body {
    background: var(--page);
    font-family: "Jost", "Futura", sans-serif;
    position: relative;
  }
  .card {
    position: absolute;
    width: 525px;
    height: 300px;
    border-radius: 22px;
    overflow: hidden;
    box-shadow: 0 6px 18px rgba(0,0,0,0.14);
  }
  /* Front side */
  .card-front {
    left: 337px;
    top: 100px;
    background: var(--card-grey);
    display: flex;
    align-items: center;
    justify-content: center;
    gap: 16px;
  }
  .brand-mark {
    width: 58px;
    height: 58px;
    border-radius: 50%;
    border: 4px solid var(--on-grey);
    flex: none;
  }
  .brand-name {
    color: var(--on-grey);
    font-weight: 500;
    font-size: 30px;
    letter-spacing: 1px;
    text-transform: uppercase;
  }
  /* Back side */
  .card-back {
    left: 337px;
    top: 500px;
    background: var(--card-white);
  }
  .base-wave { position: absolute; left: 0; bottom: 0; width: 525px; height: 300px; }
  .logo-panel {
    position: absolute;
    left: 0; top: 0;
    width: 205px;
    height: 272px;
    background: linear-gradient(90deg, var(--panel) 0%, var(--panel) 92%, #e6e6e6 100%);
    box-shadow: 4px 0 10px rgba(0,0,0,0.06);
    display: flex;
    flex-direction: column;
    align-items: center;
    justify-content: center;
    gap: 12px;
  }
  .logo-panel .brand-mark {
    width: 74px;
    height: 74px;
    border: 5px solid var(--accent-green);
    background: #ffffff;
  }
  .logo-panel .brand-name {
    color: var(--ink-mid);
    font-size: 16px;
    text-align: center;
    line-height: 1.25;
    max-width: 150px;
  }
  .contact-block {
    position: absolute;
    left: 236px;
    top: 68px;
    color: var(--ink-dark);
  }
  .person-name { font-size: 21px; font-weight: 500; }
  .person-title { font-size: 16px; color: var(--ink-mid); margin-top: 2px; }
  .contact-list { list-style: none; margin-top: 26px; }
  .contact-list li {
    display: flex;
    align-items: center;
    gap: 8px;
    font-size: 15.5px;
    color: var(--ink-mid);
    line-height: 24px;
  }
  .contact-list svg { width: 14px; height: 14px; fill: var(--accent-green); flex: none; }
</style>
</head>
<body>

  <section class="card card-front" aria-label="Card front">
    <span class="brand-mark"></span>
    <span class="brand-name">Tidewater Guidance</span>
  </section>

  <section class="card card-back" aria-label="Card back">
    <svg class="base-wave" viewBox="0 0 525 300" aria-hidden="true">
      <path d="M0,300 L0,284 Q300,276 525,248 L525,300 Z" fill="var(--band-grey)"/>
      <path d="M0,280 Q300,272 525,242 L525,249 Q300,277 0,285 Z" fill="var(--accent-green)"/>
    </svg>

    <div class="logo-panel">
      <span class="brand-mark"></span>
      <span class="brand-name">Tidewater Guidance</span>
    </div>

    <div class="contact-block">
      <h1 class="person-name">Lauren Pettigrew, MFT</h1>
      <p class="person-title">President</p>
      <ul class="contact-list">
        <li>
          <svg viewBox="0 0 16 16"><path d="M2 5c0-2 2-3 6-3s6 1 6 3v1h-3V5H5v1H2z M4 7h8l2 6H2z"/></svg>
          321-555-0164
        </li>
        <li>
          <svg viewBox="0 0 16 16"><path d="M1 3h14v10H1z M2 4l6 5 6-5" fill="none" stroke="var(--accent-green)" stroke-width="1.6"/></svg>
          Lauren@tidewaterguidance.com
        </li>
        <li>
          <svg viewBox="0 0 16 16"><circle cx="8" cy="8" r="6.5" fill="none" stroke="var(--accent-green)" stroke-width="1.4"/><path d="M1.5 8h13 M8 1.5v13 M8 1.5c-3 3-3 10 0 13 M8 1.5c3 3 3 10 0 13" fill="none" stroke="var(--accent-green)" stroke-width="1.1"/></svg>
          www.tidewaterguidance.com
        </li>
      </ul>
    </div>
  </section>

</body>
</html>
```